Business Card Design Project

Use our current logo. Clean design.

Industry/Entity Type

Business

Requirements
Must have
• Marisela DUBRANCQ
M. Law
Managing Partner

Alpenvorsa AG
Kornhalmweg 214
CH-3097 Liebefeld

M. +41 79 412 56 27
T. +41 31 928 44 10
F. +41 31 928 44 19

m.dubrancq@alpenvorsa-example.com
www.alpenvorsa-example.com

```html
<!DOCTYPE html>
<html lang="en">
<head>
<meta charset="utf-8">
<title>Alpenvorsa AG – Business Card</title>
<link rel="stylesheet" href="https://fonts.googleapis.com/css2?family=Tinos:wght@400;700&family=Open+Sans:wght@400;700&display=swap">
<style>
  :root {
    --page-bg: #e9e7e4;
    --card-black: #141414;
    --card-white: #ffffff;
    --accent-red: #d81e1e;
    --text-light: #f2f2f2;
    --text-dark: #1a1a1a;
    --rule-grey: #5a5a5a;
  }
  * { margin: 0; padding: 0; box-sizing: border-box; }
  html, body { width: 1200px; height: 800px; overflow: hidden; }
  body {
    background: var(--page-bg);
    display: flex;
    align-items: center;
    justify-content: center;
    gap: 60px;
    font-family: "Tinos", "Times New Roman", serif;
  }
  .card {
    width: 520px;
    height: 336px;
    position: relative;
    overflow: hidden;
    box-shadow: 0 6px 22px rgba(0,0,0,0.18);
  }

  /* Back side */
  .card-back {
    background: var(--card-black);
    color: var(--text-light);
    display: flex;
    flex-direction: column;
    align-items: center;
    justify-content: center;
  }
  .back-wordmark {
    display: flex;
    align-items: center;
    gap: 14px;
    font-weight: 400;
    font-size: 46px;
    letter-spacing: 3px;
    color: var(--text-light);
  }
  .wordmark-square {
    width: 20px;
    height: 20px;
    background: var(--text-light);
  }
  .back-web {
    margin-top: 26px;
    font-size: 15px;
    letter-spacing: 0.5px;
  }

  /* Front side */
  .card-front { background: var(--card-black); color: var(--text-light); }
  .front-top {
    position: absolute;
    left: 0; top: 0;
    width: 100%;
    height: 132px;
    background: var(--card-white);
    border-top: 10px solid var(--accent-red);
  }
  .front-wordmark {
    position: absolute;
    left: 30px; top: 50%;
    transform: translateY(-50%);
    display: flex;
    align-items: center;
    gap: 9px;
    font-weight: 400;
    font-size: 23px;
    letter-spacing: 2px;
    color: var(--text-dark);
  }
  .front-wordmark .wordmark-square { width: 12px; height: 12px; background: var(--text-dark); }
  .person {
    position: absolute;
    left: 310px; top: 50%;
    transform: translateY(-50%);
    color: var(--text-dark);
    font-family: "Open Sans", Arial, sans-serif;
  }
  .person-name {
    font-weight: 700;
    font-size: 16px;
    letter-spacing: 0.2px;
    white-space: nowrap;
  }
  .person-degree {
    font-size: 12px;
    font-weight: 700;
    letter-spacing: 0.5px;
    margin-top: 4px;
  }
  .person-role {
    font-size: 11px;
    letter-spacing: 0.4px;
    margin-top: 2px;
  }
  .front-bottom {
    position: absolute;
    left: 0; top: 132px;
    width: 100%;
    height: 204px;
    font-size: 13.5px;
    line-height: 1.45;
  }
  .address { position: absolute; left: 30px; top: 22px; font-style: normal; }
  .email { position: absolute; left: 30px; bottom: 24px; font-size: 12.5px; }
  .column-rule {
    position: absolute;
    left: 290px; top: 18px;
    width: 1px; height: 168px;
    background: var(--rule-grey);
  }
  .contacts { position: absolute; left: 310px; top: 42px; }
  .contacts dt { display: inline; font-weight: 700; }
  .contacts dd { display: inline; margin-left: 4px; }
  .contacts dd::after { content: ""; display: block; }
  .web { position: absolute; left: 310px; bottom: 24px; font-size: 12.5px; }
</style>
</head>
<body>

  <section class="card card-back" aria-label="Business card, back">
    <div class="back-wordmark"><span class="wordmark-square"></span>ALPENVORSA</div>
    <p class="back-web">www.alpenvorsa-example.com</p>
  </section>

  <section class="card card-front" aria-label="Business card, front">
    <header class="front-top">
      <div class="front-wordmark"><span class="wordmark-square"></span>ALPENVORSA</div>
      <div class="person">
        <p class="person-name">Marisela DUBRANCQ</p>
        <p class="person-degree">M. LAW</p>
        <p class="person-role">MANAGING PARTNER</p>
      </div>
    </header>
    <div class="front-bottom">
      <address class="address">
        Alpenvorsa AG<br>
        Kornhalmweg 214<br>
        CH-3097 Liebefeld
      </address>
      <p class="email">m.dubrancq@alpenvorsa-example.com</p>
      <span class="column-rule"></span>
      <dl class="contacts">
        <dt>M:</dt><dd>+41 79 412 56 27</dd>
        <dt>T:</dt><dd>+41 31 928 44 10</dd>
        <dt>F:</dt><dd>+41 31 928 44 19</dd>
      </dl>
      <p class="web">www.alpenvorsa-example.com</p>
    </div>
  </section>

</body>
</html>
```